Marketing Collaterals
Flyer, edm, web template, product label, brochure, vouchers
Hi Brondel,
Thanks for your new submissions. I like the look and feel of this set of collaterals. But as mentioned, no need to work on flyer and label.
And pls make the voucher generic so I can stamp the value of the voucher on it. Pls also make the voucher simpler and cleaner looking.
Thanks
HI Everyone,
Just to reiterate:
No need to work on flyer, product label, edm anymore.
Only need to work on the following in order of priority:
1) Website
2) Vouchers (1 generic version that I can rubber stamp value of voucher on it) pls take note of size - 148.5 mm x 70 mm
3) Brochure
Thanks.
Hi everyone,
I also noticed many of you used a lot of curves and wavy lines. I much prefer simple, clean cut straight lines. With a zen feel.
The closest to it now is probably #25.
The offer posters that I uploaded as well as the stock images should give you a clear idea of what I'm looking for.
Thanks again.
I also noticed that many of you used images that are not quite suitable. Either because they are too feminine, or contradicts the services we provide. Eg. our upper body massages are provided on chairs, so images of people lying on their back while receiving a massage may be misleading.
To make it easier for all, I have gone to Pixelharbor to look for suitable images. Here is the link to my lightbox http://www.pixelharbor-example.com/public_lightbox.mhtml?lightbox_id=48207615&code=3ac19b8e2d4470fa61c8e3907b15d2c4
Pls limit images to those in the light box instead.
Pls let me know if the link to the lightbox is not working.
Hi Everyone,
Hope you had a great start to the new year.
I am sorry for keeping all of you waiting. My business start up is going through some teething problems that prevented me from devoting time to work on the marketing collaterals. Thank you all for your patience and understanding.
And I thank the staff @ Plenvarta for allowing me to reopen this project.
To keep the project more focussed and simpler, I have decided to drop several of the items in the original scope of work, leaving only 3 items. Pls see below for update:
Items to work on in order of priority:
1)Website template
- I have uploaded an updated copy for the website
- Look and feel should be simple, clean and sophisticated
- Main colour will be black
- I have uploaded my business card, the label for the Dead Sea Salt packaging as well as 2 offer posters for your reference so you know what kind of look I am going for
2) Gift Vouchers
- Dimensions: 148.5 mm x 70 mm
- 4 colour x 1 colour
- back of the voucher will feature terms and conditions
- To save on print cost, I would like to have one single version of the voucher, with the flexibility to rubber stamp the value of the voucher. (pls let me know if this is not clear and I will be happy to clarify what I mean)
- Voucher value could include: $5 spa cash, $50 spa cash, 40 mins Foot Reflexology, 20 mins Upper Body Massage etc. These values will be rubber stamped prominently onto the generic voucher.
- Dimension: Open size - 210mm x 297mm
Closed size - 210mm x 99mm
- Brochure should follow the look and feel of the website
- Copy will need to be cut back quite a bit
Hope this provides clearer direction now.
Thank you and I look forward to seeing your work.
Hi to all designers who submitted your designs. I have been very bogged down by a series of unexpected issues on the business front. Hence have not devote time to work on this. Will look into this as soon as I can.
To staff of plenvarta, i understand I would normally have 7 days to decide but I need more time. I will come back as soon as I can.
Thanks to all for understanding.
Thanks to all designers who submitted your designs. Apologies for not getting back and providing feedback on your designs as I have been very busy with the opening of the shop.
Am looking through all of your work now. Will come back soon.
kindly send feedback on the above entries. thanks
Working on it :)
Dear Project Holder,
I saw your project.I am working on it.thanks.
Hi NimbusForgeArt,
Thank you for your submission.
Here are my comments:
#1 - As mentioned, the images of the ladies are not very appropriate and does not align with the offerings and image of the place we want to portray.
#2 - Same comments on the images of the ladies. Also, one side of the flyer should introduce Kelp Arbor and it's services and the other side is purely on the offers.
#3 - Many of images used are again not suitable as they are not part of our service offering and some of the fish therapy pictures feature the wrong type of fish.
Tip: Keep the creatives clean. Maybe better to have few but bigger appropriate pictures then to have many small pictures.
Hope the comments are helpful.
Thank you.
Hi Rovantoad,
I had every intention to award the job at the end. But if it makes it more secure, I have now guaranteed the job. I have also increased the prize money from $400 previously to $800 now.
Thanks for the feedback and hope to see your submission.
Hi all,
I need to add one more item:
Promotional pull up banner standee
It will feature the 2 promotional offers as stated in the flyer.
Also, pls note that for the A5 flyer, my preference is for it to be portrait rather than landscape.
Dear 7pixelcrafter and Brondel,
Thanks for your feedback. I have increased the prize money.
Hope to see your work soon.

```html
<!DOCTYPE html>
<html lang="en">
<head>
<meta charset="utf-8">
<title>Kelp Arbor – Web Template and Gift Voucher</title>
<link href="https://fonts.googleapis.com/css2?family=Lato:wght@400;700&family=Playfair+Display:ital@1&display=swap" rel="stylesheet">
<style>
:root{
  --paper:#ffffff;
  --ink:#111111;
  --black:#050505;
  --panel:#0d0d0d;
  --lime:#c6dc3a;
  --cyan:#34b5d6;
  --grey-text:#cfcfcf;
  --footer:#3b3b3b;
  --rule:#2c2c2c;
  --skin-a:#e9c7b0;
  --skin-b:#b98c72;
  --pink:#e7a8c3;
  --stone:#6e6e6e;
}
*{box-sizing:border-box;margin:0;padding:0}
html,body{width:1200px;height:869px;overflow:hidden;background:var(--paper)}
body{position:relative;font-family:"Lato",sans-serif;color:var(--ink)}
.label{position:absolute;font-size:13px;color:var(--ink)}
.abs{position:absolute}

/* website */
.site{position:absolute;left:34px;top:53px;width:645px;height:758px;background:var(--black);color:#fff}
.brand{position:absolute;left:0;right:0;top:26px;display:flex;justify-content:center;align-items:center;gap:10px}
.brand-dot{width:34px;height:34px;border-radius:50%;background:var(--lime)}
.brand-name{font-size:30px;font-weight:700;color:var(--lime);line-height:1}
.brand-tag{position:absolute;left:0;right:0;top:64px;text-align:center;font-size:10px;color:var(--lime)}
.nav{position:absolute;left:55px;top:84px;width:546px;height:18px;display:flex;background:#1a1a1a;border:1px solid var(--rule)}
.nav a{flex:1;text-align:center;font-size:10px;line-height:16px;color:#ddd;text-decoration:none;border-right:1px solid var(--rule)}
.nav a.active{background:var(--cyan);color:#fff}
.hero{position:absolute;left:55px;top:110px;width:547px;height:221px;background:linear-gradient(110deg,#f4efe9 0%,var(--skin-a) 45%,var(--skin-b) 70%,#f2ebe4 100%)}
.hero-title{position:absolute;left:20px;top:136px;font-family:"Playfair Display",serif;font-style:italic;font-size:30px;color:#4a4a4a}
.intro-h{position:absolute;left:55px;top:340px;font-size:14px;font-weight:700;color:var(--lime)}
.intro-p{position:absolute;left:55px;top:360px;width:547px;font-size:8.5px;line-height:12px;color:var(--grey-text)}
.services-h{position:absolute;left:55px;top:420px;font-size:17px;font-weight:700;color:var(--lime)}
.service{position:absolute;top:443px;width:140px}
.service h3{font-size:12px;font-weight:700;color:var(--cyan)}
.service .sub{font-size:8px;color:#fff;margin-top:2px}
.service .thumb{width:132px;height:84px;margin-top:8px}
.service p{font-size:7px;line-height:10px;color:var(--grey-text);margin-top:8px}
.more{display:block;width:40px;margin:5px 0 0 92px;background:var(--cyan);color:#fff;font-size:6px;text-align:center;line-height:9px;border-radius:2px}
.divider{position:absolute;top:440px;width:1px;height:210px;background:var(--rule)}
.footer{position:absolute;left:0;bottom:0;width:645px;height:67px;background:var(--footer)}
.footer-nav{display:flex;justify-content:center;gap:22px;margin-top:10px;font-size:10px;color:#ddd}
.footer-phone{display:flex;justify-content:center;align-items:center;gap:6px;margin-top:10px;font-size:11px;color:#ddd}

/* vouchers */
.voucher{position:absolute;left:700px;width:476px;height:180px;background:var(--black);color:#fff;overflow:hidden}
.v-front{top:84px;border-radius:6px}
.v-strip{position:absolute;left:0;top:0;width:12px;height:180px;background:linear-gradient(var(--lime),var(--cyan))}
.v-brand{position:absolute;left:30px;top:22px;display:flex;align-items:center;gap:7px}
.v-brand .brand-dot{width:22px;height:22px}
.v-brand .brand-name{font-size:20px}
.v-photo{position:absolute;top:8px;width:72px;height:72px;border-radius:50%}
.v-value{position:absolute;left:30px;top:96px;width:430px;height:58px;background:#f3f3f3;color:var(--ink);border-radius:3px}
.v-value .cap{position:absolute;left:8px;top:5px;font-size:9px}
.v-value .amt{position:absolute;left:0;right:0;top:28px;text-align:center;font-size:14px;color:#222}
.v-note{position:absolute;right:14px;bottom:7px;font-size:8px;color:#ddd}
.v-back{top:353px;height:175px}
.v-back h2{position:absolute;left:0;right:0;top:8px;text-align:center;font-size:13px;font-weight:700;color:var(--lime)}
.terms{position:absolute;left:22px;right:22px;top:28px;font-size:6px;line-height:8.5px;color:#ddd;text-align:justify}
.address{position:absolute;left:0;right:0;top:112px;text-align:center;font-size:6px;line-height:8.5px;color:#ddd}
</style>
</head>
<body>

<div class="label" style="left:34px;top:30px">webtemplate</div>
<div class="label" style="left:700px;top:62px">Voucher front</div>
<div class="label" style="left:700px;top:330px">Voucher back</div>

<main class="site">
  <div class="brand"><span class="brand-dot"></span><span class="brand-name">Kelp Arbor</span></div>
  <div class="brand-tag">Foot Reflexology and Fish Spa</div>

  <nav class="nav">
    <a class="active">Home</a><a>Services</a><a>Products</a><a>Gift Vouchers</a><a>Promotion</a><a>FAQ's</a><a>contacts</a>
  </nav>

  <div class="hero" role="img" aria-label="Photo of hands giving a foot reflexology treatment with a pink orchid">
    <div class="hero-title">Foot Reflexology</div>
  </div>

  <h1 class="intro-h">A Retreat for Body &amp; Soul</h1>
  <p class="intro-p">Step into Kelp Arbor, your personal sanctuary for complete rejuvenation, and you'll find yourself embraced by an elegant ambience that offers a calm, soothing retreat. Here you can unwind after a long day, leave daily worries behind, and let our caring therapists restore balance to body and mind. Take a seat, breathe slowly, and enjoy a moment of quiet comfort made just for you. We welcome every guest.</p>

  <h2 class="services-h">Services</h2>

  <section class="service" style="left:70px">
    <h3>Fish Spa →</h3><div class="sub">The Natural Pedicure</div>
    <div class="thumb" role="img" aria-label="Photo of feet in a fish spa pool" style="background:linear-gradient(135deg,#2f5f6e,#8fb9c4)"></div>
    <p>Experience the gentle touch of small fish that softly clean and refresh tired feet, leaving skin smooth and light.</p>
    <span class="more">read more</span>
  </section>
  <div class="divider" style="left:224px"></div>

  <section class="service" style="left:252px">
    <h3>Foot Reflexology →</h3><div class="sub">The Way to Total Wellbeing</div>
    <div class="thumb" role="img" aria-label="Photo of feet resting beside stones and a pink flower" style="background:linear-gradient(135deg,var(--stone),var(--pink))"></div>
    <p>Let our skilled hands press key points on your feet to ease tension and restore a calm sense of balance.</p>
    <span class="more">read more</span>
  </section>
  <div class="divider" style="left:410px"></div>

  <section class="service" style="left:438px">
    <h3>Upper Body Massage →</h3><div class="sub">Bust Those Cares Away...</div>
    <div class="thumb" role="img" aria-label="Photo of a seated shoulder massage" style="background:linear-gradient(135deg,#d9d9d9,var(--skin-b))"></div>
    <p>A seated massage for neck, back and shoulders that melts away stress in just a few relaxing minutes.</p>
    <span class="more">read more</span>
  </section>

  <footer class="footer">
    <div class="footer-nav"><span>Home</span><span>Services</span><span>Products</span><span>Gift Vouchers</span><span>Promotion</span><span>FAQ's</span><span>contacts</span></div>
    <div class="footer-phone">
      <svg width="14" height="14" viewBox="0 0 24 24" aria-hidden="true"><circle cx="12" cy="12" r="11" fill="none" stroke="#ddd" stroke-width="1.5"/><path d="M8 6.5l2 2-1 1.5c.8 1.7 2.3 3.2 4 4l1.5-1 2 2-1.3 1.8c-3.8-.5-7.5-4.2-8-8z" fill="#ddd"/></svg>
      <span>+65 6000 2471</span>
    </div>
  </footer>
</main>

<section class="voucher v-front">
  <div class="v-strip"></div>
  <div class="v-brand"><span class="brand-dot"></span><span class="brand-name">Kelp Arbor</span></div>
  <div class="v-photo" role="img" aria-label="Photo of pink flower and stones" style="left:240px;background:radial-gradient(circle,var(--pink),#555)"></div>
  <div class="v-photo" role="img" aria-label="Photo of a foot in a spa bowl" style="left:318px;background:radial-gradient(circle,var(--skin-a),#3d3d3d)"></div>
  <div class="v-photo" role="img" aria-label="Photo of a shoulder massage" style="left:396px;background:radial-gradient(circle,#e8e8e8,var(--skin-b))"></div>
  <div class="v-value">
    <span class="cap">Value of voucher</span>
    <span class="amt">$10 Spa cash for 20 mins Upper Body Massage</span>
  </div>
  <div class="v-note">Now available: Fish Spa and Foot Reflexology</div>
</section>

<section class="voucher v-back">
  <h2>Terms and conditions</h2>
  <p class="terms">This voucher is valid for six months from the date of issue and must be presented in full at the time of treatment. It cannot be exchanged for cash, refunded or replaced if lost, stolen or damaged. Only one voucher may be used per visit and it cannot be combined with any other promotion or discount. Advance booking is required and is subject to availability. Please arrive ten minutes before your appointment; late arrivals may have shortened sessions. Kelp Arbor reserves the right to amend these terms without prior notice. Guests with medical conditions should inform our staff before treatment begins. Any unused balance will not be carried forward to a later visit.</p>
  <div class="address">
    © Arbor Wellness Pte Ltd<br>
    Blk 48 Lantern Walk #01-12<br>
    Singapore 000482<br><br>
    Tel: +65 6000 2471<br>
    www.kelparbor-example.com
  </div>
</section>

</body>
</html>
```